Lucky Velvet Game Evenings Business Card Design

I need a business card for a fun casino entertainment business. I would like one side of the business card to convey the feel of a playing card similar to the playing card uploaded but with one logo placed horizontally across the card and the web address below it.
the information side can be slightly more plain, maybe just a stack of chips along one side or something with a casino feel.

Industry/Entity Type

Casino

Contact Information for Business Card

Lucky Velvet Game Evenings
Ted Morrowick
Director
0438 216590
ted@luckyvelvetparties.com.au

```html
<!DOCTYPE html>
<html lang="en">
<head>
<meta charset="utf-8">
<title>Lucky Velvet Game Evenings – Business Card</title>
<link rel="stylesheet" href="https://fonts.googleapis.com/css2?family=Bebas+Neue&family=Yellowtail&family=Tinos&display=swap">
<style>
  :root {
    --page-bg: #f1f1f1;
    --card-bg: #ffffff;
    --card-front-bg: #ecedee;
    --frame-line: #c9cbcd;
    --ink-dark: #2b2b2b;
    --ink-mid: #555555;
    --ink-soft: #777777;
    --decor-red: #e6c4c1;
    --decor-green: #cfe0cc;
    --decor-gold: #efe3bf;
    --shadow: rgba(0, 0, 0, 0.12);
  }
  * { box-sizing: border-box; margin: 0; padding: 0; }
  html, body {
    width: 1200px;
    height: 1000px;
    overflow: hidden;
    background: var(--page-bg);
  }
  .canvas {
    position: relative;
    width: 1200px;
    height: 1000px;
  }
  .card {
    position: absolute;
    left: 240px;
    width: 720px;
    height: 420px;
    border-radius: 22px;
    box-shadow: 0 6px 18px var(--shadow);
    overflow: hidden;
  }

  /* Front side: playing-card styled face */
  .card--front {
    top: 50px;
    background: var(--card-front-bg);
  }
  .card-frame {
    position: absolute;
    inset: 22px;
    border: 2px solid var(--frame-line);
    border-radius: 14px;
  }
  .card-frame--inner {
    inset: 30px;
    border-width: 1px;
    border-radius: 10px;
  }
  .brand-mark {
    position: absolute;
    top: 160px;
    left: 0;
    width: 100%;
    display: flex;
    align-items: center;
    justify-content: center;
    gap: 16px;
  }
  .brand-mark__dot {
    width: 30px;
    height: 30px;
    border-radius: 50%;
    background: var(--ink-dark);
  }
  .brand-mark__name {
    font-family: "Bebas Neue", sans-serif;
    font-size: 56px;
    font-weight: 400;
    letter-spacing: 1px;
    line-height: 1;
    color: var(--ink-dark);
  }
  .front-web {
    position: absolute;
    top: 290px;
    width: 100%;
    text-align: center;
    font-family: "Tinos", serif;
    font-size: 24px;
    letter-spacing: 0.5px;
    color: var(--ink-soft);
  }

  /* Information side */
  .card--back {
    top: 530px;
    background: var(--card-bg);
  }
  .back-decor {
    position: absolute;
    left: 40px;
    top: 120px;
    width: 210px;
    height: 260px;
    border-radius: 14px;
    background: linear-gradient(160deg, var(--decor-gold) 0%, var(--decor-red) 50%, var(--decor-green) 100%);
    opacity: 0.55;
  }
  .back-title {
    position: absolute;
    top: 40px;
    width: 100%;
    text-align: center;
    font-family: "Yellowtail", cursive;
    font-size: 42px;
    font-weight: 400;
    color: var(--ink-dark);
  }
  .person {
    position: absolute;
    top: 128px;
    left: 290px;
    width: 340px;
    text-align: center;
  }
  .person__name {
    font-family: "Bebas Neue", sans-serif;
    font-size: 44px;
    font-weight: 400;
    line-height: 1;
    color: var(--ink-dark);
  }
  .person__role {
    margin-top: 4px;
    font-family: "Tinos", serif;
    font-size: 18px;
    color: var(--ink-mid);
  }
  .contact {
    position: absolute;
    top: 240px;
    left: 290px;
    width: 340px;
    text-align: center;
    font-family: "Tinos", serif;
    font-size: 21px;
    line-height: 1.45;
    color: var(--ink-mid);
    list-style: none;
  }
</style>
</head>
<body>
<main class="canvas">
  <section class="card card--front" aria-label="Business card front">
    <div class="card-frame"></div>
    <div class="card-frame card-frame--inner"></div>
    <div class="brand-mark">
      <span class="brand-mark__dot"></span>
      <span class="brand-mark__name">Lucky Velvet Game Evenings</span>
    </div>
    <p class="front-web">www.luckyvelvetparties.com.au</p>
  </section>

  <section class="card card--back" aria-label="Business card information side">
    <div class="back-decor" role="img" aria-label="Faint illustration of playing cards and a stack of casino chips"></div>
    <h1 class="back-title">Lucky Velvet Game Evenings</h1>
    <div class="person">
      <p class="person__name">Ted Morrowick</p>
      <p class="person__role">director</p>
    </div>
    <ul class="contact">
      <li>phone: 0438 216590</li>
      <li>ted@luckyvelvetparties.com.au</li>
      <li>www.luckyvelvetparties.com.au</li>
    </ul>
  </section>
</main>
</body>
</html>
```